Web Design Project for Copperleaf Systems Collective

Design a webpage to replace www.copperleafsystemscollective.com.au

View the website and design a new website based on the same philosophy of the original.

The website will be fresh, simple, elegant, modern, and a hint of high degree of technical backdrop.

Please utilise the logo in the website design and keep the different contents.

Industry/Entity Type

Group

Requirements
Must have
• Must incorporate the logo which will be uploaded.

```html
<!DOCTYPE html>
<html lang="en">
<head>
<meta charset="utf-8">
<title>Copperleaf Systems Collective</title>
<link rel="stylesheet" href="https://fonts.googleapis.com/css2?family=Ubuntu:wght@400;500;700&family=Roboto+Condensed:wght@700&display=swap">
<style>
:root{
  --blue-deep:#0b4f9e;
  --blue-mid:#1b7fd3;
  --blue-light:#3fb0ec;
  --nav-text:#2d3a4a;
  --nav-active:#0d4f96;
  --yellow:#f9c623;
  --yellow-dark:#e8a90c;
  --gold:#f6d465;
  --grey-bg:#dcdcdc;
  --grey-panel:#f1f1f1;
  --text:#3a3a3a;
  --text-soft:#666;
  --white:#fff;
}
*{box-sizing:border-box;margin:0;padding:0}
html,body{width:1200px;height:1164px;overflow:hidden}
body{position:relative;font-family:"Ubuntu",sans-serif;color:var(--text);
  background:linear-gradient(#d6d6d6,#e6e6e6 40%,#d9d9d9)}
.site-header{position:absolute;left:0;top:0;width:1200px;height:571px;
  background:radial-gradient(ellipse at 50% 35%,var(--blue-light),var(--blue-mid) 45%,var(--blue-deep) 100%)}
.brand{position:absolute;left:137px;top:22px;display:flex;align-items:center;gap:14px}
.brand-dot{width:70px;height:70px;border-radius:50%;background:var(--white)}
.brand-name{font-weight:700;font-size:25px;line-height:1.15;color:var(--white);width:260px}
.social{position:absolute;left:558px;top:14px}
.social-bubble{width:94px;height:70px;border-radius:50%;background:#e9edf2;font-size:15px;font-weight:700;color:#37536f;text-align:center;padding-top:18px;line-height:1.1}
.social-icons{position:absolute;left:108px;top:46px;display:flex;gap:8px}
.social-icons span{width:26px;height:26px;border-radius:50%;background:#e8f2fb}
.social-icons span:last-child{background:#f08a1c}
.contact{position:absolute;right:130px;top:36px;text-align:right;color:var(--gold);font-weight:700;font-size:17px;line-height:1.55;padding-left:20px;border-left:1px solid rgba(255,255,255,.35)}
.contact .call{color:var(--white);font-family:"Roboto Condensed",sans-serif;font-weight:700;font-size:18px;letter-spacing:.5px}
.contact .call b{color:var(--gold)}
.main-nav{position:absolute;left:120px;top:113px;width:960px;height:65px;background:var(--white);border-radius:6px;box-shadow:0 4px 10px rgba(0,0,0,.25);display:flex;align-items:center;gap:24px;padding-left:34px}
.main-nav a{font-family:"Roboto Condensed",sans-serif;font-weight:700;font-size:17px;color:var(--nav-text);text-decoration:none;letter-spacing:.3px;white-space:nowrap}
.main-nav a.active{color:var(--nav-active)}
.search{position:absolute;right:26px;top:18px;width:180px;height:30px;border:1px solid #cfd4da;border-radius:4px;font-size:12px;color:#999;padding:7px 10px;line-height:14px}
.search svg{position:absolute;right:8px;top:7px}
.hero-text{position:absolute;left:140px;top:250px;width:395px;color:var(--white);font-size:24px;line-height:1.36}
.btn{display:inline-block;background:linear-gradient(#fcd94a,var(--yellow-dark));color:#2a2a2a;border-radius:20px;font-family:"Roboto Condensed",sans-serif;font-weight:700;text-decoration:none}
.hero-btn{position:absolute;left:144px;top:434px;width:147px;height:34px;font-size:15px;text-align:center;line-height:34px}
.slider{position:absolute;left:542px;top:213px;width:538px;height:312px;background:var(--white);border-radius:4px;padding:10px;box-shadow:0 6px 14px rgba(0,0,0,.3)}
.slider-photo{width:100%;height:100%;background:linear-gradient(100deg,#9fb4c6,#e8e4df 45%,#d8c08e 75%,#f2efe9)}
.slider-arrow{position:absolute;top:138px;width:34px;height:34px;border-radius:50%;background:rgba(255,255,255,.55);display:flex;align-items:center;justify-content:center}
.slider-arrow.prev{left:22px}.slider-arrow.next{right:22px}
.card{position:absolute;top:610px;width:306px;height:370px;background:linear-gradient(#f6f6f6,#e9e9e9);border-radius:4px;box-shadow:0 5px 10px rgba(0,0,0,.25);padding:31px}
.card-photo{width:242px;height:142px}
.card h2{font-weight:400;font-size:21px;color:#222;margin:25px 0 16px -3px}
.card p{font-size:12.5px;line-height:22px;color:var(--text-soft)}
.card ul{list-style:none;font-size:12.5px;color:var(--text-soft);line-height:23px}
.card li::before{content:"";display:inline-block;width:6px;height:6px;background:#888;transform:rotate(45deg);margin:0 12px 2px 4px}
.card .more{font-family:"Ubuntu",sans-serif;font-weight:400;font-size:11px;padding:1px 8px;border-radius:2px;margin-top:14px}
.mission{left:120px}.services{left:447px}.products{left:776px}
.product-grid{display:grid;grid-template-columns:repeat(4,48px);gap:13px 16px}
.product-grid span{width:48px;height:48px;background:var(--white);border:1px solid #ccc;box-shadow:0 1px 3px rgba(0,0,0,.2)}
.site-footer{position:absolute;left:120px;top:1011px;width:962px;height:72px;background:var(--grey-panel);border-radius:4px;box-shadow:0 3px 8px rgba(0,0,0,.2);padding:22px 22px;font-size:11px;line-height:15px}
.site-footer a{color:#333;text-decoration:none;margin-right:7px}
.footer-brand{position:absolute;right:24px;top:20px;display:flex;align-items:center;gap:6px;color:#c5c5c5;font-weight:700;font-size:18px}
.footer-brand i{width:30px;height:30px;border-radius:50%;background:#cfcfcf}
.copyright{position:absolute;left:128px;top:1100px;font-size:11px;color:#777}
</style>
</head>
<body>
<header class="site-header">
  <div class="brand"><span class="brand-dot"></span><span class="brand-name">Copperleaf Systems Collective</span></div>
  <div class="social">
    <div class="social-bubble">Social<br>Media</div>
    <div class="social-icons" aria-label="Social links"><span></span><span></span><span></span></div>
  </div>
  <div class="contact">
    <div class="call">CALL US <b>0400 555 012</b></div>
    <div>hello@copperleafsystems.com.au</div>
  </div>
  <nav class="main-nav">
    <a class="active" href="#">HOME</a><a href="#">MISSION</a><a href="#">SERVICES</a><a href="#">PRODUCTS</a><a href="#">PARTNERS</a><a href="#">SHOP</a><a href="#">BLOG</a><a href="#">CONTACT</a>
    <div class="search">Search
      <svg width="14" height="14" viewBox="0 0 14 14"><circle cx="6" cy="6" r="4.5" fill="none" stroke="#888" stroke-width="1.6"/><line x1="9.3" y1="9.3" x2="13" y2="13" stroke="#888" stroke-width="1.8"/></svg>
    </div>
  </nav>
  <p class="hero-text">We are an Electrical Engineering consulting company specializing in consultation, supply, installation and service of electrical and communications systems.</p>
  <a class="btn hero-btn" href="#">LEARN MORE</a>
  <div class="slider">
    <div class="slider-photo" role="img" aria-label="Photo of smiling support staff wearing headsets"></div>
    <span class="slider-arrow prev"><svg width="12" height="14"><path d="M9 1 3 7l6 6" fill="none" stroke="#777" stroke-width="2"/></svg></span>
    <span class="slider-arrow next"><svg width="12" height="14"><path d="M3 1l6 6-6 6" fill="none" stroke="#777" stroke-width="2"/></svg></span>
  </div>
</header>

<section class="card mission">
  <div class="card-photo" role="img" aria-label="Photo of three team members" style="background:linear-gradient(90deg,#c9c0b3,#a58e7a 40%,#d9d2c8)"></div>
  <h2>Our Mission</h2>
  <p>We are an Electrical Engineering consulting company specializing in consultation, supply, installation and service of electrical and communications systems.</p>
  <a class="btn more" href="#">Learn More</a>
</section>

<section class="card services">
  <div class="card-photo" role="img" aria-label="Photo of hands typing on a white keyboard" style="background:linear-gradient(160deg,#f3dcd4,#f7f7f7 50%,#e1e1e1)"></div>
  <h2>Our Services</h2>
  <ul><li>Maximum Business protection</li><li>Global solutions</li><li>Access Control</li><li>Intrusion detection</li></ul>
  <a class="btn more" href="#">Learn More</a>
</section>

<section class="card products">
  <div class="card-photo" role="img" aria-label="Illustration of a hand placing puzzle pieces against a sky" style="background:linear-gradient(#2f8fd6,#9fd3f2 55%,#6fb83c)"></div>
  <h2>Company Products</h2>
  <div class="product-grid" role="img" aria-label="Product category icons">
    <span></span><span></span><span></span><span></span><span></span><span></span><span></span><span></span>
  </div>
</section>

<footer class="site-footer">
  <div><a href="#">Home</a><a href="#">Mission</a><a href="#">Services</a><a href="#">Products</a><a href="#">Partners</a><a href="#">Shop</a><a href="#">Blog</a><a href="#">Contact</a></div>
  <div><a href="#">Privacy Policy</a><a href="#">Terms of Use</a></div>
  <div class="footer-brand"><i></i>Copperleaf Systems Collective</div>
</footer>
<p class="copyright">2011 - © Copperleaf Systems Collective Pty Ltd. All Rights Reserved</p>
</body>
</html>
```